Modern Informational OBGYN website

Looking for a modern Wordpress website for a general OBGYN practice in Florida with a specialty in High Risk Obstetrics. We had an old Joomla website that crashed and we lost most of the files. It was over 10 years old and needed a refresh anyway.

Our practice serves a multicultural patient population (white, black, Spanish and Indian) and we would like our website to reflect that diversity. Our company colors are sunshine yellow (#ECBF6D) often combined with black, white and steel blue (#7191BE) in the "life" part of our logo (attached) depending on the background. Our tagline is "We're specialist in You!" Overall the site should have a clean modern yet comfortable feel. One that portrays friendliness and competence. At least 6 pages (Home, Obstetrics, Gynecology, News, Patient Education and Resources). Rotating stock pictures or videos are fine for the headers of the pages if the design you're considering calls for it. Interesting and creative use of typography and icons are encouraged.

The home page should have a call to action to schedule an appointment as well as a link to our patient portal. Other than the home and news pages, the other pages should have a similar look and feel. The home page should have sections on "About Us", "Medical Staff" (with pictures and brief bio for 2 male doctors, 2 female midwives and 1 female nurse practitioner), "Services" and "Location". The news page will be a closed blog that will not allow comments or responses. Both the obstetrics and the gynecology pages will have an educational blurb on the respective topics followed by a list of our services for each topic. Would be nice on the obstetrics page to have information and graphics changes that occur during each trimester (but not necessary). The resource page will have sections on at least "Office Forms", Office Policies", "OB Guide" each with multiple downloadable PDF's. Also a section on "Insurance" with a list of all the major insurance plans that we take with links to their company websites. The address, link and map to our hospital and their website can also go on this page. The Patient Education Page can be broken into 3 sections Obstetrics, Gynecology which both will have definition of medical disorders followed by FAQ's and "Helpful Links" which would have links to other website for medical information.

That's all that I can think of right now. The above is to help guide you but I am flexible, if the website design dictates a better flow of information. Looking forward to seeing what you can come up with. Down the road, I will be looking to the winning designer to produce matching brochures, full, half and quarter page media ads to have on hand for the practices further needs.

Target Market(s)

Women looking medical services

Industry/Entity Type

Medical

Coding

Coded - Design and coding required

Number of Pages Required

5+ page

Font styles to use
Sans Serif
Script

Colors

Designer to choose colors to be used in the design.

Requirements
Must have
• None. See projects description for suggestions
Nice to have
• infographics like information on stages of pregnancy on the obstetrics page

```html
<!DOCTYPE html>
<html lang="en">
<head>
<meta charset="utf-8">
<title>Daybright OB/GYN Services</title>
<link href="https://fonts.googleapis.com/css2?family=Tinos&family=Raleway:wght@400;500;600&family=Open+Sans:ital,wght@1,600&display=swap" rel="stylesheet">
<style>
:root{
  --sun:#f1b32a;
  --ink:#1b1b1b;
  --text:#555;
  --cream:#faf6f1;
  --footer:#e9e7e6;
  --white:#fff;
  --field-line:#e3e3e3;
}
*{margin:0;padding:0;box-sizing:border-box}
html,body{width:1200px;height:3259px;overflow:hidden}
body{position:relative;background:var(--white);font-family:"Raleway",sans-serif;color:var(--text)}
.abs{position:absolute}
.serif{font-family:"Tinos",serif;color:var(--ink);font-weight:400}

/* hero */
.hero{left:0;top:0;width:1200px;height:842px;
  background:
    radial-gradient(ellipse 170px 120px at 770px 780px,rgba(232,196,170,.95),rgba(232,196,170,0)),
    radial-gradient(ellipse 200px 230px at 720px 460px,rgba(176,208,236,.95),rgba(176,208,236,0)),
    radial-gradient(ellipse 90px 110px at 760px 230px,rgba(236,204,178,.9),rgba(236,204,178,0)),
    radial-gradient(ellipse 120px 90px at 1080px 470px,rgba(52,96,200,.75),rgba(52,96,200,0)),
    radial-gradient(ellipse 180px 420px at 1070px 560px,rgba(250,252,255,.95),rgba(250,252,255,0)),
    radial-gradient(ellipse 110px 140px at 1090px 170px,rgba(70,48,40,.55),rgba(70,48,40,0)),
    radial-gradient(ellipse 110px 130px at 760px 190px,rgba(170,118,70,.55),rgba(170,118,70,0)),
    linear-gradient(100deg,#f3f2ef 0%,#eceae5 40%,#e4e6ea 60%,#dde6ef 100%)}
.nav-box{left:80px;top:39px;width:1040px;height:100px;background:var(--white);border-radius:4px}
.brand{display:flex;align-items:center;gap:8px;left:108px;top:62px}
.brand-dot{width:22px;height:22px;border-radius:50%;background:var(--sun)}
.brand-name{font-weight:600;font-size:25px;color:var(--sun);letter-spacing:.5px;line-height:1}
.brand-sub{font-weight:600;font-size:9px;color:var(--sun);letter-spacing:3px;margin-top:4px}
.nav a{position:absolute;top:83px;font-size:14px;color:#333;text-decoration:none;letter-spacing:.2px}
.hero-title{left:87px;top:318px;font-size:74px;line-height:66px}
.btn{background:var(--sun);color:var(--white);display:flex;align-items:center;justify-content:center;border-radius:2px}
.hero-btn{left:85px;top:552px;width:286px;height:58px;font-size:20px;font-weight:500;color:#222;letter-spacing:.5px}

/* welcome */
.welcome-img{left:57px;top:939px;width:570px;height:379px;
  background:
    radial-gradient(ellipse 110px 90px at 200px 90px,rgba(120,200,235,.9),rgba(120,200,235,0)),
    radial-gradient(ellipse 150px 110px at 330px 340px,rgba(240,240,245,.95),rgba(240,240,245,0)),
    radial-gradient(ellipse 220px 200px at 170px 270px,rgba(40,120,220,.9),rgba(40,120,220,0)),
    radial-gradient(ellipse 160px 240px at 400px 150px,rgba(80,150,225,.8),rgba(80,150,225,0)),
    linear-gradient(135deg,#8b97a3,#5d86b6 50%,#c8d2dc)}
.welcome-title{left:675px;top:951px;font-size:45px;line-height:41px}
.welcome-copy{left:677px;top:1064px;width:450px;font-size:14px;line-height:22.4px;color:#666}
.welcome-btn{left:675px;top:1256px;width:160px;height:44px;font-size:14px}

/* services */
.services{left:0;top:1415px;width:1200px;height:699px;background:var(--cream)}
.services-title{left:0;top:1495px;width:1200px;text-align:center;font-size:48px;padding-left:10px}
.services-copy{left:190px;top:1579px;width:820px;text-align:center;font-size:14px;line-height:18px;color:#666}
.card-img{top:1676px;width:325px;height:207px}
.card-title{top:1906px;width:325px;text-align:center;font-size:26px}
.card-copy{top:1950px;width:325px;text-align:center;font-size:14px;line-height:18px;color:#777}
.dot{top:2034px;width:8px;height:8px;background:#ccc}
.dot.on{background:var(--sun)}

/* appointment */
.appt-bg{left:0;top:2114px;width:1200px;height:807px;background:linear-gradient(90deg,#f6f8fb 0%,#eef2f7 40%,#e6ebf1 100%)}
.appt-photo{left:532px;top:2114px;width:668px;height:807px;
  background:
    radial-gradient(ellipse 100px 130px at 300px 120px,rgba(40,34,34,.75),rgba(40,34,34,0)),
    radial-gradient(ellipse 90px 110px at 285px 230px,rgba(232,196,168,.9),rgba(232,196,168,0)),
    radial-gradient(ellipse 100px 130px at 520px 190px,rgba(150,100,70,.6),rgba(150,100,70,0)),
    radial-gradient(ellipse 80px 100px at 530px 280px,rgba(236,204,180,.9),rgba(236,204,180,0)),
    radial-gradient(ellipse 140px 80px at 260px 580px,rgba(150,165,180,.8),rgba(150,165,180,0)),
    radial-gradient(ellipse 230px 380px at 300px 560px,rgba(252,253,255,.95),rgba(252,253,255,0)),
    radial-gradient(ellipse 180px 360px at 560px 560px,rgba(245,246,250,.9),rgba(245,246,250,0)),
    linear-gradient(120deg,#e8edf3,#d2dae4 45%,#eef1f5)}
.appt-title{left:114px;top:2220px;font-size:46px}
.appt-sub{left:94px;top:2285px;font-family:"Open Sans",sans-serif;font-style:italic;font-weight:600;font-size:19px;color:var(--sun)}
.field{height:30px;background:var(--white);border:1px solid var(--field-line);font-size:13px;font-style:italic;color:#999;padding-left:16px;display:flex;align-items:center}
.appt-btn{left:95px;top:2781px;width:160px;height:44px;font-size:14px}

/* footer */
.footer{left:0;top:2921px;width:1200px;height:301px;background:var(--footer)}
.follow{left:133px;top:3076px;font-size:16px;font-weight:600;color:#222;letter-spacing:.5px}
.social{top:3100px;width:30px;height:30px;border:2px solid var(--sun);border-radius:50%}
.f-head{font-family:"Tinos",serif;font-size:19px;color:#222;letter-spacing:.5px}
.f-link{font-size:13px;color:#444;display:flex;align-items:center;gap:8px}
.f-link::before{content:"";width:0;height:0;border-left:5px solid var(--sun);border-top:3px solid transparent;border-bottom:3px solid transparent}
.f-contact{font-size:13px;color:#333;line-height:16px}
.bar{left:0;top:3222px;width:1200px;height:37px;background:var(--sun);display:flex;align-items:center;justify-content:center;font-size:12px;color:#5a4512}
</style>
</head>
<body>

<!-- Hero -->
<div class="abs hero" role="img" aria-label="Photo of a smiling pregnant woman in a light blue top with a female doctor holding a blue clipboard in a bright clinic"></div>
<div class="abs nav-box"></div>
<div class="abs brand">
  <span class="brand-dot"></span>
  <div><div class="brand-name">DAYBRIGHT</div><div class="brand-sub">OB/GYN SERVICES</div></div>
</div>
<nav class="nav">
  <a style="left:375px">HOME</a>
  <a style="left:454px">OBSTETRICS</a>
  <a style="left:579px">GYNECOLOGY</a>
  <a style="left:714px">NEWS</a>
  <a style="left:795px">PATIENT EDUCATION</a>
  <a style="left:979px">RESOURCES</a>
</nav>
<h1 class="abs serif hero-title">We're<br>SPECIALIST<br>in You!</h1>
<a class="abs btn hero-btn">MAKE APPOINTMENT</a>

<!-- Welcome -->
<div class="abs welcome-img" role="img" aria-label="Photo of a masked nurse in blue scrubs holding a patient's hand during delivery"></div>
<h2 class="abs serif welcome-title">Welcome to<br>Daybright Care</h2>
<p class="abs welcome-copy">Sed ut perspiciatis unde omnis iste natus error sit voluptatem accusantium doloremque laudantium, totam rem aperiam, eaque ipsa quae ab illo inventore veritatis et quasi architecto beatae vitae dicta sunt explicabo. Nemo enim ipsam voluptatem quia voluptas sit aspernatur aut odit aut fugit, sed quia consequuntur magni dolores eos qui ratione voluptatem sequi nesciunt. Neque porro quisquam est, qui dolorem ipsum quia dolor sit amet, consectetur, adipisci</p>
<a class="abs btn welcome-btn">Appointment now</a>

<!-- Services -->
<div class="abs services"></div>
<h2 class="abs serif services-title">Our Services</h2>
<p class="abs services-copy">Lorem ipsum dolor sit amet, consectetur adipiscing elit, sed do eiusmod tempor incididunt ut labore et dolore ma<br>gna aliqua. Ut enim ad minim veniam, quis nostrud exercitation ullamco</p>

<div class="abs card-img" style="left:87px;background:radial-gradient(ellipse 80px 90px at 230px 30px,rgba(150,80,50,.6),rgba(150,80,50,0)),radial-gradient(ellipse 90px 120px at 80px 110px,rgba(130,130,140,.85),rgba(130,130,140,0)),radial-gradient(ellipse 90px 60px at 80px 30px,rgba(110,60,45,.7),rgba(110,60,45,0)),linear-gradient(120deg,#b7b2ae,#e8e5e1 55%,#f5f3f0)" role="img" aria-label="Photo of a doctor listening to a pregnant patient's belly with a stethoscope"></div>
<h3 class="abs serif card-title" style="left:87px">Gynecology</h3>
<p class="abs card-copy" style="left:87px">Lorem ipsum dolor sit amet, consectetur<br>adipiscing elit, sed do eiusmod tempor</p>

<div class="abs card-img" style="left:438px;background:radial-gradient(ellipse 70px 40px at 80px 115px,rgba(80,170,170,.7),rgba(80,170,170,0)),radial-gradient(ellipse 80px 90px at 190px 130px,rgba(215,170,140,.8),rgba(215,170,140,0)),radial-gradient(ellipse 60px 120px at 300px 80px,rgba(220,140,60,.6),rgba(220,140,60,0)),linear-gradient(120deg,#dcd8d3,#f3f0ec 50%,#c9b9a8)" role="img" aria-label="Photo of a doctor writing notes during a consultation"></div>
<h3 class="abs serif card-title" style="left:438px">Fertility medication</h3>
<p class="abs card-copy" style="left:438px">incididunt ut labore et dolore magna aliqua.<br>Ut enim ad minim veniam, quis nostrud</p>

<div class="abs card-img" style="left:795px;background:radial-gradient(ellipse 160px 50px at 200px 180px,rgba(190,160,130,.85),rgba(190,160,130,0)),radial-gradient(ellipse 40px 40px at 155px 50px,rgba(60,70,90,.7),rgba(60,70,90,0)),radial-gradient(ellipse 50px 80px at 50px 60px,rgba(150,120,100,.6),rgba(150,120,100,0)),linear-gradient(120deg,#c8d2dc,#eef2f5 50%,#dfe6ec)" role="img" aria-label="Photo of a prenatal ultrasound scan in an exam room"></div>
<h3 class="abs serif card-title" style="left:795px">Prenadal ultrasound</h3>
<p class="abs card-copy" style="left:795px">dolore ma gna aliqua. Ut enim ad minim<br>veniam, quis nostrud exercitation</p>

<span class="abs dot on" style="left:588px"></span>
<span class="abs dot" style="left:616px"></span>
<span class="abs dot" style="left:648px"></span>

<!-- Appointment -->
<div class="abs appt-bg"></div>
<div class="abs appt-photo" role="img" aria-label="Photo of a female doctor with glasses reviewing a clipboard with a patient"></div>
<h2 class="abs serif appt-title">Fix Appointment</h2>
<p class="abs appt-sub">Get your family off to a smiling start&nbsp; Form</p>
<div class="abs field" style="left:100px;top:2355px;width:366px">Your Name</div>
<div class="abs field" style="left:100px;top:2418px;width:366px">Your Email</div>
<div class="abs field" style="left:100px;top:2484px;width:366px">Your Phone numer</div>
<div class="abs field" style="left:98px;top:2545px;width:366px">Select Service</div>
<div class="abs field" style="left:98px;top:2606px;width:182px">Select Date</div>
<div class="abs field" style="left:289px;top:2606px;width:173px">Select Time</div>
<div class="abs field" style="left:92px;top:2682px;width:366px">Your Message Here</div>
<a class="abs btn appt-btn">Check Availability</a>

<!-- Footer -->
<div class="abs footer"></div>
<div class="abs brand" style="left:118px;top:2990px">
  <span class="brand-dot"></span>
  <div><div class="brand-name">DAYBRIGHT</div><div class="brand-sub">OB/GYN SERVICES</div></div>
</div>
<div class="abs follow">FOLLOW US</div>
<span class="abs social" style="left:134px"></span>
<span class="abs social" style="left:171px"></span>
<span class="abs social" style="left:208px"></span>
<span class="abs social" style="left:245px"></span>

<div class="abs f-head" style="left:442px;top:3003px">LINKS</div>
<div class="abs f-link" style="left:442px;top:3051px">Home</div>
<div class="abs f-link" style="left:442px;top:3077px">Obstetrics</div>
<div class="abs f-link" style="left:442px;top:3105px">Gynecology</div>
<div class="abs f-link" style="left:609px;top:3051px">News</div>
<div class="abs f-link" style="left:609px;top:3077px">Patient Education</div>
<div class="abs f-link" style="left:609px;top:3105px">Resources</div>

<div class="abs f-head" style="left:896px;top:3005px">CONTACT US</div>
<svg class="abs" style="left:896px;top:3053px" width="14" height="18" viewBox="0 0 14 18"><path d="M7 0C3.1 0 0 3 0 6.8 0 11.5 7 18 7 18s7-6.5 7-11.2C14 3 10.9 0 7 0z" fill="var(--sun)"/><circle cx="7" cy="6.8" r="2.6" fill="var(--footer)"/></svg>
<div class="abs f-contact" style="left:923px;top:3053px">1420 Harbor View Road<br>Coral Springs, Florida 33065</div>
<svg class="abs" style="left:896px;top:3104px" width="16" height="16" viewBox="0 0 16 16"><path d="M3.2 0.5l2.6 3.2-1.6 2a10 10 0 0 0 6.1 6.1l2-1.6 3.2 2.6-1.6 2.6C6.6 15.6 0.4 9.4 0.6 2.1z" fill="var(--sun)"/></svg>
<div class="abs f-contact" style="left:923px;top:3105px">555 014 2290</div>
<svg class="abs" style="left:896px;top:3139px" width="16" height="12" viewBox="0 0 16 12"><rect width="16" height="12" fill="var(--sun)"/><path d="M0 0l8 6 8-6" fill="none" stroke="var(--footer)" stroke-width="1.4"/></svg>
<div class="abs f-contact" style="left:923px;top:3137px">hello@daybrightcare.com</div>

<div class="abs bar">© 2018 Company Name &nbsp;|&nbsp; All Right Reserved</div>

</body>
</html>
```